Business Card Design Project

Design a business card for a new entity that is in the OTC (over-the-counter-derivative brokering business-Financial Services.
The card should be clean a professional looking. We encourage designers to think pro-actively, fresh and innovative, but also keep in mind that only 2 things are important. a)that the card look professional b)that it is somehow memorable.

We have a new logo which we will upload and will want the Trident symbol in the logo to be raised OR not have the symbol raised and plan on having the word " BROKERAGE SERVICES" raised that stands out and will look sharp.

Along with uploading the new logo which MUST be incorperated, I am also going to upload 3 different business cards of other businesses to use only as guild-lines since I think they are clean and professional looking BUT I encourage all to be pro-active and creative on their own.

Industry/Entity Type

Business

Requirements
Must have
• 1. MUST HAVE THE NEW LOGO WHICH WILL BE UPLOADED
2. MUST HAVE A VERSION SIMILAR TO THE 3 DIFFERENT BUSINESS CARDS I WILL UPLOAD, BUT EACH DESIGNER MUST ONLY THESE THIS FORMAT AS A BACK-UP AND BE CREATIVE ON THEIR OWN FIRST. ALSO WHEN LOOKING AT THE CARDS WHICH I UPLOAD TO USE AS A GUILD-LINE KEEP IN MIND THAT THESE ARE KESTRAVEL 300 COMPANIES SO DO NOT MIMIC ONLY USE FOR IDEAS.
Nice to have
• these are the 3 different other biz cards to look at for some reference

```html
<!DOCTYPE html>
<html lang="en">
<head>
<meta charset="utf-8">
<title>Halcyon Brokerage Services – Business Card</title>
<link rel="stylesheet" href="https://fonts.googleapis.com/css2?family=Arimo:wght@400;700&display=swap">
<style>
  :root {
    --gold: #e2b83a;
    --gold-light: #efcd55;
    --gold-deep: #c9991f;
    --ink: #3a3a3c;
    --ink-soft: #5a5a5c;
    --paper: #ffffff;
    --stage: #ecebe8;
    --rule: rgba(80, 60, 10, 0.35);
  }
  * { box-sizing: border-box; margin: 0; padding: 0; }
  html, body { width: 1200px; height: 900px; overflow: hidden; }
  body {
    background: var(--stage);
    font-family: "Arimo", Arial, sans-serif;
    color: var(--ink);
    display: flex;
    flex-direction: column;
    align-items: center;
    justify-content: center;
    gap: 56px;
  }
  .card {
    width: 640px;
    height: 366px;
    position: relative;
    overflow: hidden;
    box-shadow: 0 10px 28px rgba(0,0,0,0.18);
  }

  /* Front */
  .card-front {
    background: linear-gradient(135deg, var(--gold-deep) 0%, var(--gold) 45%, var(--gold-light) 100%);
    display: flex;
    flex-direction: column;
    align-items: center;
    justify-content: center;
  }
  .brand { display: flex; align-items: center; gap: 16px; }
  .brand-dot {
    width: 46px; height: 46px; border-radius: 50%;
    background: var(--ink);
  }
  .brand-name {
    font-size: 58px; font-weight: 400; letter-spacing: 4px;
    color: var(--ink); line-height: 1;
  }
  .brand-tagline {
    margin-top: 10px;
    font-size: 15px; letter-spacing: 7px; text-transform: uppercase;
    color: #f7e7a8;
  }
  .front-web {
    margin-top: 34px;
    font-size: 14px; letter-spacing: 4px; color: var(--ink);
  }

  /* Back */
  .card-back { background: var(--paper); }
  .back-main {
    position: absolute; left: 0; top: 0; width: 470px; height: 100%;
  }
  .back-logo {
    position: absolute; left: 0; top: 0; width: 470px; height: 196px;
    display: flex; flex-direction: column; justify-content: center;
    padding-left: 40px;
  }
  .back-logo .brand-dot { width: 34px; height: 34px; }
  .back-logo .brand-name { font-size: 44px; letter-spacing: 3px; }
  .back-logo .brand-tagline {
    color: var(--gold-deep); font-size: 12px; letter-spacing: 6px;
    margin-top: 8px; padding-left: 50px;
  }
  .back-band {
    position: absolute; left: 0; top: 196px; width: 470px; height: 170px;
    background: linear-gradient(90deg, var(--gold-deep), var(--gold));
    padding: 26px 40px;
    color: var(--paper);
  }
  .band-pointer {
    position: absolute; left: 120px; top: -1px;
    width: 28px; height: 14px;
  }
  .person { font-size: 22px; color: var(--ink); }
  .person .role { font-size: 13px; margin-left: 6px; }
  .contact-line { font-size: 13px; margin-top: 6px; color: var(--paper); }
  .back-web { font-size: 17px; font-weight: 700; color: var(--ink); margin-top: 12px; }

  .back-side {
    position: absolute; right: 0; top: 0; width: 170px; height: 100%;
    background: linear-gradient(180deg, var(--gold-light), var(--gold));
    padding: 34px 18px;
    display: flex; flex-direction: column; justify-content: space-between;
    font-size: 12px; line-height: 1.6; color: var(--paper);
  }
  .side-divider { border-top: 1px solid var(--rule); }
</style>
</head>
<body>

  <section class="card card-front" aria-label="Card front">
    <div class="brand">
      <span class="brand-dot"></span>
      <span class="brand-name">HALCYON</span>
    </div>
    <div class="brand-tagline">Brokerage Services</div>
    <div class="front-web">www.HalcyonBrokerage.com</div>
  </section>

  <section class="card card-back" aria-label="Card back">
    <div class="back-main">
      <div class="back-logo">
        <div class="brand">
          <span class="brand-dot"></span>
          <span class="brand-name">HALCYON</span>
        </div>
        <div class="brand-tagline">Brokerage Services</div>
      </div>
      <div class="back-band">
        <svg class="band-pointer" viewBox="0 0 28 14" aria-hidden="true">
          <polygon points="0,0 28,0 14,14" fill="#5a5a5c"/>
        </svg>
        <div class="person">Alex Morgan <span class="role">Manager</span></div>
        <div class="contact-line">Mobile: 000 000 000</div>
        <div class="contact-line">Email: alex@halcyonbrokerage.com</div>
        <div class="back-web">www.HalcyonBrokerage.com</div>
      </div>
    </div>
    <aside class="back-side">
      <address style="font-style:normal">
        00 Your Street<br>
        000000 000 000 0000<br>
        PO Box 000
      </address>
      <div class="side-divider"></div>
      <div>
        Ph: +00 7 0000 0000<br>
        Fax: + 00 7 000 0000
      </div>
    </aside>
  </section>

</body>
</html>
```